Fernvale Pharmacy opening

We want to have a double sided 5.5"x8.5" flyer for a new Pharmacy opening in a well known strip mall in the neighborhood and we are planning to mail it to neighbors homes.

Want to put the outside pharmacy picture on the main side of the flyer and a coupon with 25% off towards an OTC product on the back in addition to the info below (preferably in a sort of bulletin points not a list (something like the 2 examples attached).

Colors to be red like the exterior sign and blue like the interior wall paint:

Front side should have:
Fernvale pharmacy
Your locally owned and operated pharmacy around the corner.
317-4082 Tarrow rd.
Brisket hollow plaza
T. 604 827 5530 (call or text)
F. 604-827-5532

Free prescription delivery
Text us for refills
Specialized compounding
Customized compression stockings

The back side should have:

Do you forget taking your medications! We offer multiple compliance packaging options at no additional cost.
Had shingles before or worried to have it? travelling soon? check our vaccinations options!
Suffering side effects? We are experienced to check your medications interactions & different coverage options.
Hard time monitoring your blood pressure? Trying to stop smoking? we can always help.

FEELING BETTER STARTS HERE

```html
<!DOCTYPE html>
<html lang="en">
<head>
<meta charset="utf-8">
<title>Fernvale Pharmacy – Opening Flyer</title>
<link rel="stylesheet" href="https://fonts.googleapis.com/css2?family=Open+Sans:wght@400;600;700;800&family=Oswald:wght@500;600&display=swap">
<style>
  :root {
    --red: #e31b23;
    --red-dark: #c3141b;
    --navy: #2b3a55;
    --navy-deep: #1f2b42;
    --ink: #2a3550;
    --white: #ffffff;
    --page: #e9e9ec;
    --rule: #c9ccd3;
  }
  * { box-sizing: border-box; margin: 0; padding: 0; }
  html, body { width: 1200px; height: 1102px; overflow: hidden; }
  body {
    background: var(--page);
    font-family: "Open Sans", Arial, sans-serif;
    color: var(--ink);
    position: relative;
  }
  .card {
    position: absolute;
    left: 200px;
    width: 800px;
    height: 518px;
    background: var(--white);
    overflow: hidden;
    box-shadow: 0 3px 12px rgba(0,0,0,.18);
  }
  .card--front { top: 22px; }
  .card--back { top: 562px; }
  .card > svg.backdrop { position: absolute; inset: 0; }
  .abs { position: absolute; }

  /* brand */
  .brand { display: flex; align-items: center; gap: 14px; }
  .brand__dot { width: 92px; height: 92px; border-radius: 50%; background: var(--red); flex: none; }
  .brand__name {
    font-weight: 800; color: var(--red); font-size: 30px; line-height: 1.05;
    letter-spacing: .5px; text-transform: uppercase;
  }

  /* front */
  .tagline { left: 30px; top: 168px; width: 320px; font-size: 19px; font-weight: 600; line-height: 1.3; color: var(--ink); }
  .now-open { left: 28px; top: 258px; font-weight: 800; font-size: 46px; color: var(--white); letter-spacing: 1px; }
  .perks { left: 28px; top: 326px; list-style: none; }
  .perks li { display: flex; align-items: center; gap: 10px; height: 34px; margin-bottom: 2px; color: var(--white); font-size: 18px; font-weight: 600; white-space: nowrap; }
  .perks .ico { width: 30px; height: 30px; border-radius: 50%; background: var(--red); border: 2px solid var(--white); flex: none; display: flex; align-items: center; justify-content: center; }
  .inset-photo {
    left: 372px; top: 268px; width: 150px; height: 150px; border-radius: 50%;
    border: 5px solid var(--white);
    background: linear-gradient(180deg,#3a4d73 0%,#d8d6d0 55%,#b8a98e 100%);
  }
  .badge {
    left: 486px; top: 358px; width: 106px; height: 106px; border-radius: 50%;
    background: var(--red); border: 3px solid var(--white); color: var(--white);
    text-align: center; padding-top: 20px; white-space: nowrap;
  }
  .badge__big { font-family: "Oswald", sans-serif; font-weight: 600; font-size: 26px; line-height: 1; }
  .badge__small { font-size: 11px; font-weight: 700; line-height: 1.25; margin-top: 5px; }
  .contact-bar { left: 26px; top: 474px; display: flex; align-items: center; gap: 12px; color: var(--white); font-family: "Oswald", sans-serif; font-weight: 600; font-size: 21px; letter-spacing: .5px; white-space: nowrap; }
  .contact-bar svg { flex: none; }
  .front-address { right: 14px; top: 482px; font-size: 13.5px; font-weight: 600; color: var(--ink); white-space: nowrap; }

  /* back */
  .tips { left: 18px; top: 100px; width: 400px; list-style: none; }
  .tip { position: relative; height: 72px; margin-bottom: 1px; }
  .tip__head {
    position: absolute; left: 0; top: 0; height: 24px; padding: 0 38px 0 14px;
    background: var(--red); color: var(--white); font-size: 11.5px; font-weight: 700; line-height: 24px;
    clip-path: polygon(0 0, 90% 0, 100% 100%, 0 100%); z-index: 2; white-space: nowrap;
  }
  .tip__body {
    position: absolute; left: 8px; top: 20px; width: 372px; height: 46px;
    background: var(--white); border-radius: 0 24px 24px 0;
    font-size: 11px; line-height: 1.3; color: var(--ink); padding: 8px 70px 0 12px;
  }
  .tip__icon { position: absolute; right: 16px; top: 8px; }
  .slogan { left: 28px; top: 418px; color: var(--white); font-weight: 700; font-size: 18px; letter-spacing: .5px; white-space: nowrap; }
  .back-call { left: 24px; top: 470px; display: flex; align-items: center; gap: 12px; color: var(--white); font-family: "Oswald", sans-serif; font-weight: 600; font-size: 22px; letter-spacing: .5px; white-space: nowrap; }
  .staff-photo {
    left: 396px; top: 300px; width: 120px; height: 218px; border-radius: 56px 56px 0 0;
    background: linear-gradient(180deg,#7a5a44 0%,#d9b49a 30%,#f3f3f3 55%,#e2e4e8 100%);
  }
  .mail-to { left: 506px; top: 40px; font-size: 16px; line-height: 1.35; color: #222; }
  .mail-to__name { color: var(--red); font-weight: 700; font-size: 16px; }
  .stamp { left: 700px; top: 40px; width: 78px; height: 72px; border: 1px solid #bbb; }
  .address-lines { left: 505px; top: 200px; width: 270px; }
  .address-lines span { display: block; height: 42px; border-bottom: 1px solid var(--rule); }
</style>
</head>
<body>

<!-- FRONT -->
<section class="card card--front" aria-label="Flyer front">
  <svg class="backdrop" width="800" height="518" viewBox="0 0 800 518" aria-hidden="true">
    <defs>
      <linearGradient id="navyFade" x1="0" y1="0" x2="1" y2="1">
        <stop offset="0" stop-color="#34466a"/>
        <stop offset="1" stop-color="#1f2b42"/>
      </linearGradient>
    </defs>
    <polygon points="0,300 460,268 800,300 800,470 0,470" fill="url(#navyFade)"/>
    <polygon points="0,252 310,236 326,292 0,312" fill="var(--red)"/>
    <path d="M448,0 C372,140 372,330 450,470 L430,470 C350,330 352,140 424,0 Z" fill="var(--navy)"/>
    <path d="M462,0 C388,140 388,330 466,470 L452,470 C372,330 374,140 448,0 Z" fill="var(--red)"/>
    <polygon points="0,462 480,448 500,518 0,518" fill="var(--red)"/>
  </svg>

  <div class="abs" role="img" aria-label="Photo of the pharmacy storefront with a pharmacist helping a customer"
       style="left:0;top:0;width:800px;height:470px;clip-path:path('M466,0 H800 V470 H466 C388,330 388,140 466,0 Z');background:linear-gradient(160deg,#b9b2a6 0%,#8f8a84 40%,#c9ccd4 70%,#6f7f9c 100%);"></div>
  <div class="abs inset-photo" role="img" aria-label="Photo of the pharmacy interior shelves"></div>

  <div class="abs brand" style="left:26px;top:24px;">
    <span class="brand__dot"></span>
    <span class="brand__name">Fernvale<br>Pharmacy</span>
  </div>
  <p class="abs tagline">Your locally owned and operated pharmacy around the corner.</p>
  <h1 class="abs now-open">NOW OPEN</h1>

  <ul class="abs perks">
    <li><span class="ico"><svg width="18" height="12" viewBox="0 0 18 12"><rect x="0" y="1" width="11" height="8" fill="#fff"/><path d="M11 4h4l3 3v2h-7z" fill="#fff"/><circle cx="4" cy="10" r="2" fill="#fff"/><circle cx="14" cy="10" r="2" fill="#fff"/></svg></span>Free prescription delivery</li>
    <li><span class="ico"><svg width="16" height="14" viewBox="0 0 16 14"><path d="M1 1h14v9H6l-4 3v-3H1z" fill="#fff"/></svg></span>Text us for refills</li>
    <li><span class="ico"><svg width="14" height="14" viewBox="0 0 14 14"><path d="M1 6h12a6 6 0 0 1-12 0z" fill="#fff"/><rect x="8" y="0" width="2" height="7" transform="rotate(30 9 3)" fill="#fff"/></svg></span>Specialized compounding</li>
    <li><span class="ico"><svg width="12" height="16" viewBox="0 0 12 16"><path d="M3 0h5v9l3 3v4H4l-2-3z" fill="#fff"/></svg></span>Customized compression stockings</li>
  </ul>

  <div class="abs badge">
    <div class="badge__big">25% OFF</div>
    <div class="badge__small">towards an<br>OTC product</div>
  </div>

  <div class="abs contact-bar">
    <span>CALL OR TEXT</span>
    <svg width="16" height="24" viewBox="0 0 16 24"><rect x="1" y="1" width="14" height="22" rx="3" fill="none" stroke="#fff" stroke-width="2.5"/><circle cx="8" cy="19" r="1.5" fill="#fff"/></svg>
    <span>604 827 5530&nbsp;&nbsp;F. 604-827-5532</span>
  </div>
  <p class="abs front-address">317-4082 Tarrow rd. Brisket hollow plaza</p>
</section>

<!-- BACK -->
<section class="card card--back" aria-label="Flyer back">
  <svg class="backdrop" width="800" height="518" viewBox="0 0 800 518" aria-hidden="true">
    <defs>
      <linearGradient id="navyBack" x1="0" y1="0" x2="1" y2="1">
        <stop offset="0" stop-color="#34466a"/>
        <stop offset="1" stop-color="#1f2b42"/>
      </linearGradient>
    </defs>
    <path d="M0,92 H400 C455,150 470,300 440,518 H0 Z" fill="url(#navyBack)"/>
    <path d="M300,0 H330 C460,80 490,300 450,518 H438 C476,300 448,90 300,0 Z" fill="var(--navy)"/>
    <path d="M336,0 H352 C478,90 502,300 462,518 H452 C490,300 464,90 336,0 Z" fill="var(--red)"/>
    <path d="M0,458 H360 a24,24 0 0 1 0,48 H0 Z" fill="var(--red)"/>
  </svg>

  <div class="abs brand" style="left:18px;top:4px;">
    <span class="brand__dot" style="width:82px;height:82px;"></span>
    <span class="brand__name" style="font-size:28px;">Fernvale<br>Pharmacy</span>
  </div>

  <ul class="abs tips">
    <li class="tip">
      <span class="tip__head">Do you forget taking your medications!</span>
      <p class="tip__body">We offer multiple compliance packaging options at no additional cost.
        <svg class="tip__icon" width="36" height="28" viewBox="0 0 36 28"><ellipse cx="11" cy="16" rx="9" ry="7" fill="none" stroke="var(--navy)" stroke-width="2.5"/><ellipse cx="25" cy="12" rx="9" ry="7" fill="var(--navy)"/><line x1="5" y1="21" x2="17" y2="11" stroke="var(--navy)" stroke-width="2"/></svg></p>
    </li>
    <li class="tip">
      <span class="tip__head">Had shingles before or worried to have it?</span>
      <p class="tip__body" style="padding-top:13px;">Travelling soon? Check our vaccinations options!
        <svg class="tip__icon" width="22" height="32" viewBox="0 0 22 32" style="top:6px;"><rect x="7" y="0" width="8" height="6" fill="none" stroke="var(--navy)" stroke-width="2"/><rect x="1" y="6" width="20" height="24" rx="3" fill="var(--navy)"/></svg></p>
    </li>
    <li class="tip">
      <span class="tip__head">Suffering side effects?</span>
      <p class="tip__body">We are experienced to check your medications interactions &amp; different coverage options.
        <svg class="tip__icon" width="28" height="32" viewBox="0 0 28 32" style="top:6px;"><rect x="2" y="2" width="18" height="24" fill="none" stroke="var(--navy)" stroke-width="2"/><rect x="6" y="5" width="18" height="24" fill="var(--navy)"/><circle cx="22" cy="26" r="6" fill="var(--navy)" stroke="#fff" stroke-width="1.5"/><path d="M19 26l2 2 4-4" stroke="#fff" stroke-width="1.5" fill="none"/></svg></p>
    </li>
    <li class="tip">
      <span class="tip__head">Hard time monitoring your blood pressure?</span>
      <p class="tip__body" style="padding-top:13px;">Trying to stop smoking? We can always help.
        <svg class="tip__icon" width="26" height="34" viewBox="0 0 26 34" style="top:5px;"><path d="M4 2v10a7 7 0 0 0 14 0V2" fill="none" stroke="var(--navy)" stroke-width="2"/><path d="M11 19v7a6 6 0 0 0 12 0v-6" fill="none" stroke="var(--navy)" stroke-width="2"/><circle cx="23" cy="17" r="3" fill="none" stroke="var(--navy)" stroke-width="2"/></svg></p>
    </li>
  </ul>

  <p class="abs slogan">FEELING BETTER STARTS HERE</p>

  <div class="abs staff-photo" role="img" aria-label="Photo of a smiling pharmacist in a white coat with arms crossed"></div>

  <div class="abs back-call">
    <span>CALL OR TEXT</span>
    <svg width="16" height="24" viewBox="0 0 16 24"><rect x="1" y="1" width="14" height="22" rx="3" fill="none" stroke="#fff" stroke-width="2.5"/><circle cx="8" cy="19" r="1.5" fill="#fff"/></svg>
    <span>604 827 5530</span>
  </div>

  <div class="abs mail-to">
    <p class="mail-to__name">Fernvale pharmacy</p>
    <p>317-4082 Tarrow rd.<br>Brisket hollow plaza</p>
  </div>
  <div class="abs stamp"></div>
  <div class="abs address-lines"><span></span><span></span><span></span><span></span></div>
</section>

</body>
</html>
```